Corporate Branding - Web and Print

A UK based company will like to use an existing logo to create branding materials for all marketing related documents, including business card, prints, letterhead, Website, Twitter, Facebook, Instagram logo etc. This company serves high-end clientele in the fashion, health and wellness and as such high quality and class is of utmost importance.
Where the logo can be modernised without losing its character then experiment. The main thing is to have a corporate branding which can be used later for brochures, Business Plan infographics.
The prominent colour within the organisation is burnt orange with no secondary colour. However if you believe a secondary colour is needed then use it, otherwise keep it simple and classy. Any chosen colours have to match perfectly.
Target Market(s)
High net worth individuals
Industry/Entity Type
Health And Wellness
Contact Information for Business Card
classy
Look and feel
Each slider illustrates characteristics of the customer's brand and the style your logo design should communicate.

```html
<!DOCTYPE html>
<html lang="en">
<head>
<meta charset="utf-8">
<title>Velora Business Card</title>
<link rel="stylesheet" href="https://fonts.googleapis.com/css2?family=Roboto:wght@400;500;700&family=Roboto+Condensed:wght@500;700&display=swap">
<style>
  :root {
    --bg: #2b2b2b;
    --orange: #f7961f;
    --orange-back: #ec9020;
    --paper: #f1f1f1;
    --swoosh-grey: #c6c6c6;
    --white: #ffffff;
  }
  * { margin: 0; padding: 0; box-sizing: border-box; }
  html, body { width: 1200px; height: 960px; overflow: hidden; }
  body { background: var(--bg); position: relative; font-family: "Roboto", sans-serif; }

  .card {
    position: absolute;
    width: 600px;
    height: 342px;
    border-radius: 22px;
    overflow: hidden;
  }
  .card--front { left: 314px; top: 114px; background: var(--paper); }
  .card--back  { left: 311px; top: 472px; background: var(--orange-back); }

  .front-shapes { position: absolute; inset: 0; }

  .contact {
    position: absolute;
    left: 37px;
    top: 30px;
    color: var(--white);
  }
  .contact__name {
    font-family: "Roboto Condensed", sans-serif;
    font-weight: 700;
    font-size: 22px;
    line-height: 24px;
  }
  .contact__title {
    font-family: "Roboto Condensed", sans-serif;
    font-weight: 500;
    font-size: 16px;
    line-height: 20px;
  }
  .contact__address {
    margin-top: 12px;
    font-size: 14px;
    line-height: 18px;
  }
  .contact__list { list-style: none; margin-top: 8px; }
  .contact__item {
    display: flex;
    align-items: center;
    gap: 6px;
    font-size: 14px;
    line-height: 19px;
  }
  .contact__icon { width: 14px; height: 14px; flex: none; fill: var(--white); }

  .brand {
    position: absolute;
    right: 50px;
    top: 252px;
    display: flex;
    align-items: center;
    gap: 10px;
    color: var(--orange);
    font-weight: 700;
    font-size: 40px;
    letter-spacing: 1px;
  }
  .brand__dot { width: 30px; height: 30px; border-radius: 50%; background: var(--orange); }

  .back-brand {
    position: absolute;
    left: 0; right: 0;
    top: 125px;
    text-align: center;
    color: var(--white);
    font-weight: 700;
    font-size: 64px;
    letter-spacing: 3px;
  }
  .back-web {
    position: absolute;
    left: 0; right: 0;
    top: 290px;
    text-align: center;
    color: var(--white);
    font-size: 14px;
    letter-spacing: 4px;
  }
</style>
</head>
<body>

<section class="card card--front">
  <svg class="front-shapes" width="600" height="342" viewBox="0 0 600 342">
    <path d="M46 342 C220 300 360 170 381 0 L410 0 C385 185 265 300 95 342 Z" fill="var(--swoosh-grey)"/>
    <path d="M0 0 H381 C360 170 220 300 46 342 H0 Z" fill="var(--orange)"/>
    <path d="M92 296 C250 250 368 170 406 0 C385 180 275 262 92 296 Z" fill="var(--orange)"/>
  </svg>

  <div class="contact">
    <h1 class="contact__name">DANIEL HART</h1>
    <p class="contact__title">CEO/FOUNDER</p>
    <p class="contact__address">4120 Willow Crescent<br>Maplewood, Oregon 21830</p>
    <ul class="contact__list">
      <li class="contact__item">
        <svg class="contact__icon" viewBox="0 0 24 24"><path d="M6.6 10.8a15 15 0 0 0 6.6 6.6l2.2-2.2c.3-.3.7-.4 1-.2 1.1.4 2.3.6 3.6.6.6 0 1 .4 1 1V20c0 .6-.4 1-1 1A17 17 0 0 1 3 4c0-.6.4-1 1-1h3.5c.6 0 1 .4 1 1 0 1.3.2 2.5.6 3.6.1.3 0 .7-.2 1z"/></svg>
        555 214 7730
      </li>
      <li class="contact__item">
        <svg class="contact__icon" viewBox="0 0 24 24"><path d="M7 1h10a2 2 0 0 1 2 2v18a2 2 0 0 1-2 2H7a2 2 0 0 1-2-2V3a2 2 0 0 1 2-2zm0 3v14h10V4zm5 15.5a1 1 0 1 0 0 2 1 1 0 0 0 0-2z"/></svg>
        555 381 6402
      </li>
      <li class="contact__item">
        <svg class="contact__icon" viewBox="0 0 24 24"><path d="M6 2h12v6H6zM3 9h18a1 1 0 0 1 1 1v7h-4v5H6v-5H2v-7a1 1 0 0 1 1-1zm5 6v5h8v-5z"/></svg>
        555 907 5518
      </li>
      <li class="contact__item">
        <svg class="contact__icon" viewBox="0 0 24 24"><path d="M2 5h20v14H2zm2 2v.5l8 5 8-5V7l-8 5z"/></svg>
        daniel@velora.com
      </li>
      <li class="contact__item">
        <svg class="contact__icon" viewBox="0 0 24 24"><path d="M12 2a10 10 0 1 0 0 20 10 10 0 0 0 0-20zm-1 17.9A8 8 0 0 1 4.2 10L9 15v1a2 2 0 0 0 2 2zm6.9-2.5A2 2 0 0 0 16 16h-1v-3a1 1 0 0 0-1-1H8v-2h2a1 1 0 0 0 1-1V7h2a2 2 0 0 0 2-2v-.4a8 8 0 0 1 2.9 12.8z"/></svg>
        www.velora.com
      </li>
    </ul>
  </div>

  <div class="brand"><span class="brand__dot"></span>VELORA</div>
</section>

<section class="card card--back">
  <div class="back-brand">VELORA</div>
  <p class="back-web">www.velora.com</p>
</section>

</body>
</html>
```